Business Card Design Project : Tidewell Press

In preparation for market launch, Whistler's Tidewell Press require the development of a business card. Tidewell Press is a Community online publishing web portal. We provide the the city of Whistler located in B.C. (Canada) business directories, News, Classified ads, News, Events and blogs etc.

The main focus of the brand is to help local businesses to corporate with their online advertisement and marketing. Meeting our clients face to face is a must (B2B).

Target Market(s)

The target market is B2B customers. Business Owners to Marketing, advertising Managers

Industry/Entity Type

Business

Requirements
Must have
• - The business card will be two sided.
the BACK side will have our logo which consist of (icon, url,slogan) submited. The logo will be middle and centred.

The FRONT side should have company details:

Company Legal Name: FERNDALE TIDEWELL PRESS

Owen Marsk
Director of Sales & Marketing

www.ferndaletidewell.biz
owen@ferndaletidewell.biz

Phone: 555 014 3826
#2817 - 562 E. Harlow Ave.
Vancouver, B.C. K7P2R4 Canada
Nice to have
• - For the "FRONT" side of our business card. You can separate or re-arrange with our logo components (icon, logo,slogan). It does not have to be together.

Also our company legal name is rather long so arrange or organize the name in a way to make it shorter. Your experience and creativity will have to come in play.
Should not have
• should not have other colors beside logo color and black text (2 colors). Also nothing Three dimensional

```html
<!DOCTYPE html>
<html lang="en">
<head>
<meta charset="utf-8">
<title>Ferndale Tidewell Press – Business Card</title>
<link rel="stylesheet" href="https://fonts.googleapis.com/css2?family=Didact+Gothic&family=Open+Sans:wght@700&display=swap">
<style>
  :root {
    --brand-blue: #1a7fd1;
    --ink: #111111;
    --card: #ffffff;
    --backdrop: #e9e7e3;
    --globe: #ececec;
  }
  * { box-sizing: border-box; margin: 0; padding: 0; }
  html, body { width: 1200px; height: 1200px; overflow: hidden; }
  body {
    background: var(--backdrop);
    font-family: "Didact Gothic", Arial, sans-serif;
    color: var(--ink);
  }
  .card {
    position: absolute;
    left: 180px;
    width: 840px;
    height: 480px;
    background: var(--card);
    box-shadow: 0 4px 14px rgba(0,0,0,0.12);
    overflow: hidden;
  }
  .card--front { top: 90px; }
  .card--back { top: 630px; }

  .front__band {
    position: absolute;
    left: 0;
    background: var(--brand-blue);
  }
  .front__band--top { top: 40px; width: 330px; height: 140px; }
  .front__band--name {
    top: 250px; width: 370px; height: 190px;
    display: flex; align-items: center; justify-content: center;
  }
  .front__company {
    font-size: 27px;
    line-height: 1.35;
    letter-spacing: 1px;
    text-align: center;
    color: var(--ink);
  }
  .front__globe {
    position: absolute;
    left: 420px; top: 20px;
    width: 420px; height: 420px;
  }
  .front__details {
    position: absolute;
    left: 400px; top: 80px;
    width: 410px;
    text-align: center;
    font-size: 23px;
    line-height: 1.4;
  }

  .back__logo {
    position: absolute;
    inset: 0;
    display: flex;
    flex-direction: column;
    align-items: center;
    justify-content: center;
    gap: 24px;
  }
  .back__mark {
    width: 110px; height: 110px;
    border-radius: 50%;
    background: var(--brand-blue);
  }
  .back__name {
    font-family: "Open Sans", Arial, sans-serif;
    font-weight: 700;
    font-size: 40px;
    color: var(--ink);
  }
</style>
</head>
<body>
  <section class="card card--front" aria-label="Business card front">
    <div class="front__band front__band--top"></div>
    <div class="front__band front__band--name">
      <p class="front__company">FERNDALE<br>TIDEWELL PRESS</p>
    </div>
    <svg class="front__globe" viewBox="0 0 420 420" role="img" aria-label="Faint globe decoration behind contact details">
      <circle cx="210" cy="210" r="200" fill="var(--globe)"/>
    </svg>
    <div class="front__details">
      <p class="front__person">Owen Marsk</p>
      <p class="front__title">Director of Sales &amp; Marketing</p>
      <p class="front__web">www.ferndaletidewell.biz</p>
      <p class="front__email">owen@ferndaletidewell.biz</p>
      <p class="front__phone">Phone 555 014 3826</p>
      <p class="front__address">#2817 - 562 E. Harlow Ave.</p>
      <p class="front__city">Vancouver, B.C. K7P2R4 Canada</p>
    </div>
  </section>

  <section class="card card--back" aria-label="Business card back">
    <div class="back__logo">
      <div class="back__mark"></div>
      <p class="back__name">www.ferndaletidewell.biz</p>
    </div>
  </section>
</body>
</html>
```